(draft #51)
please have the below adjustment in your design and they are:
- please change the slide color to become the same color as business card color background.
-#9 the folder inside is not shown kindly try to include if you can.
-please include an A4 Envelope, CD cover, Invoice & Flyer it is very important.
(draft #54)
-in the cd cover please include the address.
-the word oil changing service is needed below each logo.
-in the business card will you enlarge the name and push the address to the right little bit.
-please include an A4 Envelope, Invoice & Flyer it is very important.
(draft #56)
i would like to have some adjustment please and they are:
-in the letter head please will you spread the address horizontally and place it below or at the lower of the letterhead.
-in the Envelope will you take out the phone, fax, mobile and email from the upper side and place it in the lower side.
-in the folder with pocket there is no need for the mobile number and email
-please include an A4 Envelope & Flyer it is very important.
We need data for flyer.
kindly provide it.
please include all stationery like draft 59 and 60.
-please include an A4 Envelope, CD, & Flyer it is very important.
kindly delete the tilted designs logo only the horizontal drops.
but thanks again for your quick action.
thanks again
1- Please include a Folder with 1 or 2 pockets
2- master & theme slides for power point if possible.
i have uploaded the Al and eps files as per your requests and i am hoping to see good designs from you.

```html
<!DOCTYPE html>
<html lang="en">
<head>
<meta charset="utf-8">
<title>Oilvera business card</title>
<link rel="stylesheet" href="https://fonts.googleapis.com/css2?family=Arimo:ital,wght@0,400;0,700;1,700&display=swap">
<style>
  :root {
    --stage: #2b2b2b;
    --card-white: #ffffff;
    --brand-red: #a3191b;
    --brand-tan: #9a7650;
    --ink: #222222;
    --red-dark: #7e0b0d;
    --red-mid: #b01c1a;
    --red-light: #d6352a;
    --faint: rgba(200, 70, 50, 0.10);
  }
  html, body {
    margin: 0;
    padding: 0;
    width: 1200px;
    height: 511px;
    overflow: hidden;
    background: var(--stage);
    font-family: "Arimo", Arial, sans-serif;
  }
  .stage {
    position: relative;
    width: 1200px;
    height: 511px;
  }
  .card-front {
    position: absolute;
    left: 24px;
    top: 48px;
    width: 569px;
    height: 415px;
    background: var(--card-white);
    border-radius: 28px;
    overflow: hidden;
  }
  .brand {
    position: absolute;
    left: 30px;
    top: 70px;
    display: flex;
    align-items: center;
    gap: 12px;
  }
  .brand-dot {
    width: 40px;
    height: 40px;
    border-radius: 50%;
    background: var(--brand-red);
  }
  .brand-name {
    font-size: 56px;
    font-weight: 700;
    color: var(--brand-red);
    letter-spacing: -1px;
    line-height: 1;
  }
  .brand-tagline {
    position: absolute;
    left: 140px;
    top: 140px;
    font-size: 16px;
    color: var(--brand-tan);
  }
  .decor-circle {
    position: absolute;
    left: 390px;
    top: 210px;
    width: 170px;
    height: 170px;
    border-radius: 50%;
    background: var(--faint);
  }
  .person {
    position: absolute;
    left: 324px;
    top: 124px;
  }
  .person-name {
    margin: 0;
    font-size: 20px;
    font-weight: 700;
    font-style: italic;
    color: var(--ink);
  }
  .person-role {
    margin: 6px 0 0;
    font-size: 16px;
    color: var(--ink);
  }
  .contact {
    position: absolute;
    left: 324px;
    top: 242px;
    font-size: 15px;
    line-height: 19px;
    color: var(--ink);
  }
  .contact p { margin: 0; }
  .contact .gap { margin-top: 19px; }
  .contact .label { display: inline-block; width: 18px; }

  .card-back {
    position: absolute;
    left: 605px;
    top: 132px;
    width: 571px;
    height: 348px;
    border-radius: 28px;
    background: linear-gradient(90deg, var(--red-dark) 0%, var(--red-mid) 55%, var(--red-light) 100%);
    overflow: hidden;
  }
  .back-band {
    position: absolute;
    left: 115px;
    top: 146px;
    width: 341px;
    height: 72px;
    background: linear-gradient(90deg, var(--red-mid) 0%, var(--red-light) 60%, #e8553f 100%);
    display: flex;
    align-items: center;
    justify-content: center;
    gap: 10px;
  }
  .back-dot {
    width: 24px;
    height: 24px;
    border-radius: 50%;
    background: #ffffff;
  }
  .back-name {
    font-size: 36px;
    font-weight: 700;
    color: #ffffff;
    letter-spacing: -0.5px;
  }
</style>
</head>
<body>
<main class="stage">
  <section class="card-front">
    <div class="brand">
      <span class="brand-dot"></span>
      <span class="brand-name">Oilvera</span>
    </div>
    <div class="brand-tagline">Oil Changing Service</div>
    <div class="decor-circle" role="img" aria-label="Faint brand drop mark in the background"></div>
    <div class="person">
      <p class="person-name">Eng. Tariq M. Al-Harbi</p>
      <p class="person-role">Partner</p>
    </div>
    <div class="contact">
      <p>P.O.Box 48213</p>
      <p>Zip Code 23417 Jeddah</p>
      <p>Kingdom of Saudi Arabia</p>
      <p class="gap"><span class="label">P</span>+966-2-6571390</p>
      <p><span class="label">C</span>+966-551234876</p>
      <p><span class="label">F</span>+966-2-6571390</p>
      <p><span class="label">E</span>t.harbi@oilvera.example</p>
    </div>
  </section>

  <section class="card-back">
    <div class="back-band">
      <span class="back-dot"></span>
      <span class="back-name">Oilvera</span>
    </div>
  </section>
</main>
</body>
</html>
```